Coffee Company 1lb coffee bag design

Coffee Bag Design Size ( bag size 12 -16oz / 340 -454 grams / 1lb - dimensions) THE BAG IS GUSSETTED - meaning it has 4sides , like the bags shown in the attachments

* recommend text located at the bottom of the brief added July 9 th

We need a design for a retail 1lb coffee bag to package our Artisan handcrafted roasted coffee beans. The design we choose will be the standard 'look' for our freshly roasted coffee. We have our logo and need to incorporate that into an original, overall design that includes areas for text boxes on the front, back and sides. We have provided a draft of the text at the bottom of the brief to be incorporated in the design. One text box on the front will remain blank. This is where we will adhere a label that will describe the particular coffee in the package. And blank text box on the back to print a bar code.
(Side of the bag : one side of the bag would be our company story (details can be found on our web site) and the other side panel brewing instruction. I would be able to provide the txt for the 'story' and 'brewing instructions' as needed)

These are our preliminary thoughts and are open minded to other options.
We want the design to convey that our coffee is an ethically sourced , locally hand roasted in small batches , freshly roasted, sustainable, socially and environmentally responsible.

This bag will be the our main core bag for use with all the Blends / Roasts so it will need to be starting point for our overall bag design branding. We are very open to all and any creative ideas..
Ideally we would like to use a crisp white gloss bag - the logo would be the main focal point with an area below for where we would place our sticker - roast / blend details .we will be to using a sticker on the front of the bag to identify the various roasts / blends we offer until a point of having a different bag for each coffee. We don't want the bag the appear 'busy' as we prefer images over covering the whole bag with a photo.. the design needs to be crisp , clean , not overall busy, classy , using inspiration perhaps from the logo , harrow mountain range , blue ocean, green trees .... our customers enjoy the finer things in life and our brand is more of a luxury product.
Who we are:
We are a Artisan coffee roaster located in the village of Fernhollow. Our hand crafted roasted coffee is ethically sourced , locally roasted in small batches to ensure freshness in every cup. please check out our web site for further details on the company. Again , we are open and looking forward to seeing some fantastic core bag design. we will be looking for the opportunity to develop stickers for each blends in the future...

www.fernhollowcoffeeco.example

attached is the logo files and other bags that have caught our interest ... have some fun!

TEXT FOR: SIDE #1, SIDE #2 , BACK OF THE BAG

FYI - this text is still currently in DRAFT but will allow us to get an overall look for each design...

One side of the coffee bag

Revised draft of the text - updated July19th

THE STORY OF

THE FERNHOLLOW

COFFEE COMPANY,

Nestled beneath the two majestic peaks of the Harrow Mountains along the scenic Cedar Reach highway, is the picturesque village of Fernhollow. This small waterfront community on Kestrel Sound’s North Shore boasts a synchronicity between snowcapped mountains that feed twinkling creeks which meander through lush green forests and lead to the beautiful ocean. This was our inspiration to create Fernhollow Coffee Company and to share our passion for the perfect cup of coffee as reflected in each of our roasts. Our artisan roasted coffee is ethically sourced, using the highest quality Arabica beans then locally roasted in small batches to ensure freshness and the finest flavor. May the coffee you are about to enjoy, enhance your day as you experience the essence of Fernhollow.

-------------------------------------------------

Fernhollow Coffee Company

PO BOX 862

Fernhollow BC

V0N 4K7

the other Side of Bag

KEYS TO BREWING

THE PERFECT CUP

FRESHNESS

Always use freshly roasted (Fernhollow Coffee Company)

beans and within 1-2 weeks of purchase.

STORING

Your coffee has 4 enemies:

Heat, Moisture, Light & Air

Keep your coffee cool, dry and dark in an

airtight container for maximum flavour.

GRINDING

Grind beans just before

brewing. Select the best

grind for each brewing method:

Espresso = Finer Grind

Filtered = Medium Grind

French Press = Coarse Grind

BREWING

Water I Ratio I Temperature

Water: Fresh, cold, filtered water

Ratio: Use 2 rounded tablespoons

of coffee per 8 oz of water.

Temperature: Heat water between 90 – 96 C

Adjust brewing methods to your personal taste.

For more information about

brewing the perfect cup of coffee,

visit our website at

www.fernhollowcoffeeco

(ADD RBGT logo - to be provided)

Back of the bag

"The roasts I create for Fernhollow Coffee Company are a reflection of my commitment to craft the perfect cup of coffee. I hope it is the finest coffee you'll ever enjoy."
- Doran Whitlock,
Founder & Master Roaster, Fernhollow Coffee Company

Visit us our website to learn more including ordering your freshly roasted coffees

(ADD miniature Fernhollow Coffee Company logo)

Like us on Friendpage

htpp://www.friendpage.example/fernhollowcoffeeco

Follow us on Chirpline

Fernhollow Coffee @fernhollowbrew

send us an email

info@fernhollowcoffeeco.example
Updates

Design Team, just a reminder the bag design is for a gusseted bag ( see brief for details and images ) and not for a pouch bag as what is being submitted to me ? All current designs received so far are the wrong style of bag.

Update effective July 19th, 2014. Please see Brief for revised text for Keys to Brewing, The Story and back side of bag. Thanks.

Reason: Still working with a few designers with text and design - need more time Starting to narrow our selection down soon

Reason: Need to extend to add French to package design

Target Market(s)

coffee drinkers with a mature palate for Arabica Beans , ethically sourced

Font styles to use
Other font styles liked:
• same font as logo ?

Colors
0893cd
33a6d7
85cae6
85acd3
3176b5
0455a3
ffffff
cee9f5
eaf1f6

Requirements
Must have
• logo is the main image on front of bag , space for the sticker that will describe the type of bean / roast / blend
Nice to have
• white bag , logo has strong presents front and middle of the bag. crisp clean not busy designs
Should not have
• package should not be 'too busy' it is the core for all roasts and should stand for the roasting company

no cartoon pictures and un authorized clip art

```html
<!DOCTYPE html>
<html lang="en">
<head>
<meta charset="utf-8">
<title>Fernhollow Coffee Company – French Roast Bag Dieline</title>
<link href="https://fonts.googleapis.com/css2?family=Belleza&family=Marcellus&display=swap" rel="stylesheet">
<style>
  :root {
    --bag-blue: #0455a3;
    --bag-blue-mid: #3176b5;
    --sky: #85cae6;
    --sky-pale: #cee9f5;
    --mist: #eaf1f6;
    --white: #ffffff;
    --label-tan: #c49a6c;
    --label-ink: #4a2a14;
    --logo-brown: #4e2c17;
    --logo-cream: #f3ead8;
    --caption: #a7a7a7;
    --ink: #2a2a2a;
  }
  * { margin: 0; padding: 0; box-sizing: border-box; }
  html, body { width: 1200px; height: 783px; overflow: hidden; background: var(--white); }
  .canvas { position: relative; width: 1200px; height: 783px; background: var(--white); font-family: "Belleza", sans-serif; }

  .panel-caption { position: absolute; top: 42px; font-size: 15px; color: var(--caption); letter-spacing: 1px; text-align: center; }

  .panel { position: absolute; top: 71px; height: 666px; overflow: hidden; }
  .panel--front { left: 68px; width: 304px; background: var(--bag-blue); }
  .panel--rh { left: 372px; width: 228px; background: var(--bag-blue); color: var(--white); text-align: center; }
  .panel--back { left: 600px; width: 308px; background: var(--white); border: 1px solid #d8dde3; text-align: center; color: var(--ink); }
  .panel--lh { left: 908px; width: 220px; background: var(--bag-blue); color: var(--white); text-align: center; }

  /* Front */
  .front-sky { position: absolute; left: 38px; top: 0; width: 236px; height: 597px;
    background: linear-gradient(180deg, var(--sky-pale) 0%, var(--sky) 55%, var(--sky-pale) 100%); }
  .front-swirls { position: absolute; top: 0; width: 62px; height: 597px;
    background: linear-gradient(180deg, rgba(8,147,205,.35), rgba(49,118,181,.55), rgba(8,147,205,.35)); }
  .front-swirls--left { left: 38px; }
  .front-swirls--right { left: 212px; }
  .brand-mark { position: absolute; left: 0; width: 304px; top: 110px; text-align: center; }
  .brand-mark__disc { width: 180px; height: 180px; border-radius: 50%; margin: 0 auto; background: var(--logo-cream); border: 10px solid var(--logo-brown); }
  .brand-mark__name { margin-top: 16px; font-size: 34px; color: var(--logo-brown); letter-spacing: 1px; }
  .roast-label { position: absolute; left: 91px; top: 468px; width: 130px; height: 76px; background: var(--label-tan);
    font-family: "Marcellus", serif; color: var(--label-ink); font-size: 22px; line-height: 26px; text-align: center; padding-top: 12px; }
  .net-weight { position: absolute; left: 0; width: 304px; top: 560px; text-align: center; color: var(--label-ink); font-family: "Marcellus", serif; font-size: 16px; }

  /* Sides */
  .side-title { font-size: 11.5px; line-height: 15px; margin-top: 22px; letter-spacing: .2px; }
  .side-title--large { font-size: 14px; line-height: 18px; }
  .side-copy { font-size: 8.6px; line-height: 11.5px; padding: 0 26px; margin-top: 11px; }
  .side-rule { width: 150px; margin: 14px auto 0; border-top: 1px dashed rgba(255,255,255,.7); }
  .side-heading { font-size: 15px; margin-top: 10px; letter-spacing: .5px; }
  .star-rule { font-size: 9px; letter-spacing: 2px; margin-top: 8px; opacity: .85; }
  .side-ornament { width: 44px; height: 22px; margin: 14px auto 0;
    background: linear-gradient(90deg, rgba(133,202,230,.2), rgba(206,233,245,.75), rgba(133,202,230,.2)); border-radius: 12px; }
  .gusset { position: absolute; left: 0; bottom: 0; }

  /* Back */
  .back-swirls { position: absolute; left: 0; top: 0; width: 200px; height: 240px;
    background: radial-gradient(ellipse at 30% 40%, rgba(133,202,230,.45), rgba(206,233,245,.2) 60%, rgba(255,255,255,0) 75%); }
  .back-mark { position: absolute; left: 0; width: 306px; top: 222px; }
  .back-mark__disc { width: 96px; height: 96px; border-radius: 50%; margin: 0 auto; background: var(--logo-cream); border: 6px solid var(--logo-brown); }
  .back-mark__name { margin-top: 6px; font-size: 21px; color: var(--logo-brown); }
  .back-text { position: absolute; left: 0; width: 306px; top: 392px; }
  .back-quote { font-size: 14.5px; line-height: 19px; padding: 0 30px; }
  .back-stars { font-size: 10px; letter-spacing: 2.5px; color: var(--bag-blue-mid); margin-top: 10px; }
  .back-copy { font-size: 10.5px; line-height: 13px; margin-top: 10px; padding: 0 16px; }
  .back-copy--tight { margin-top: 8px; }
</style>
</head>
<body>
<main class="canvas">
  <div class="panel-caption" style="left:68px;width:304px;">FRONT</div>
  <div class="panel-caption" style="left:372px;width:228px;">RH SIDE</div>
  <div class="panel-caption" style="left:600px;width:308px;">BACK</div>
  <div class="panel-caption" style="left:908px;width:220px;">LH SIDE</div>

  <section class="panel panel--front">
    <div class="front-sky" role="img" aria-label="Light sky-blue panel behind the brand mark"></div>
    <div class="front-swirls front-swirls--left" role="img" aria-label="Blue floral swirl ornaments climbing the left edge"></div>
    <div class="front-swirls front-swirls--right" role="img" aria-label="Blue floral swirl ornaments climbing the right edge"></div>
    <div class="brand-mark">
      <div class="brand-mark__disc"></div>
      <div class="brand-mark__name">FERNHOLLOW</div>
    </div>
    <div class="roast-label">FRENCH<br>ROAST</div>
    <div class="net-weight">12 oz.</div>
  </section>

  <section class="panel panel--rh">
    <h2 class="side-title">THE STORY OF THE<br>FERNHOLLOW COFFEE COMPANY</h2>
    <p class="side-copy">Nestled beneath the two majestic peaks of the Harrow Mountains along the scenic Cedar Reach highway, is the picturesque village of Fernhollow.</p>
    <p class="side-copy">This small waterfront community on Kestrel Sound's North Shore boasts a synchronicity between snowcapped mountains feeding twinkling creeks meandering through lush green forests and leading to the beautiful ocean.</p>
    <p class="side-copy">This was our inspiration to create the Fernhollow Coffee Company and to share our passion for the perfect cup of coffee as reflected in each of our roasts.</p>
    <p class="side-copy">Our Artisan coffee is ethically sourced, using the highest quality Arabica beans then locally roasted in small batches to ensure freshness and the finest flavor.</p>
    <p class="side-copy">May the coffee you are about to enjoy, enhance your day as you experience the essence of Fernhollow.</p>
    <div class="side-rule"></div>
    <p class="side-copy">Fernhollow Coffee Company<br>PO BOX 862<br>Fernhollow BC<br>V0N 4K7<br>www.fernhollowcoffeeco.example</p>
    <div class="side-rule" style="margin-top:6px;"></div>
    <div class="side-ornament" role="img" aria-label="Small light-blue swirl ornament"></div>
    <svg class="gusset" width="228" height="110" viewBox="0 0 228 110">
      <polyline points="0,110 114,4 228,110" fill="none" stroke="#cee9f5" stroke-width="1.2" stroke-dasharray="5 4"/>
    </svg>
  </section>

  <section class="panel panel--back">
    <div class="back-swirls" role="img" aria-label="Faint light-blue floral swirl ornament"></div>
    <div class="back-mark">
      <div class="back-mark__disc"></div>
      <div class="back-mark__name">FERNHOLLOW</div>
    </div>
    <div class="back-text">
      <p class="back-quote">We hope that you will be inspired by our roasts as much as we were inspired to create them.</p>
      <div class="back-stars">* * * * * * * * * * * * * * * * * * * *</div>
      <p class="back-copy">Visit us our website to learn more including ordering your freshly roasted coffees!</p>
      <p class="back-copy back-copy--tight">www.fernhollowcoffeeco.example</p>
      <p class="back-copy back-copy--tight">Like us on Friendpage:<br>htpp://www.friendpage.example/fernhollowcoffeeco</p>
      <p class="back-copy back-copy--tight">Follow us on Chirpline:<br>Fernhollow Coffee @fernhollowbrew</p>
      <p class="back-copy back-copy--tight">Send us an email:<br>info@fernhollowcoffeeco.example</p>
    </div>
  </section>

  <section class="panel panel--lh">
    <h2 class="side-title side-title--large">KEYS TO BREWING<br>THE PERFECT CUP FRESHNESS</h2>
    <p class="side-copy">Always try to purchase your coffee at the peak of its freshness. For best results, purchase often and in smaller quantities (1-2 weeks supply max.)</p>
    <div class="star-rule">* * * * * * * * * * * *</div>
    <h3 class="side-heading">STORING</h3>
    <p class="side-copy" style="margin-top:4px;">There are four enemies for your coffee: Oxygen, moisture, light and heat…</p>
    <p class="side-copy">So we keep your coffee dry, cool, dark and airtight for maximum taste</p>
    <div class="star-rule">* * * * * * * * * * * *</div>
    <h3 class="side-heading">GRINDING</h3>
    <p class="side-copy" style="margin-top:4px;">Grind fresh just before brewing. Select the best grind for each brew method</p>
    <p class="side-copy">Espresso = Finer Grind<br>Drip Coffees = Medium Grind<br>French Press Coffees = Coarse Grind</p>
    <div class="star-rule">* * * * * * * * * * * *</div>
    <h3 class="side-heading">BREWING</h3>
    <p class="side-copy" style="margin-top:4px;">Water I Ratio I Temperature I Time<br>Water: Fresh, cold, filtered water<br>Ratio: Use two rounded tablespoons of coffee per 8 oz. of water.<br>Adjust to meet your personal needs</p>
    <p class="side-copy">Time: Use whatever method is right for you, some common methods:</p>
    <p class="side-copy">Espresso = 20-22 seconds<br>Pour Over = 2-3 minutes<br>French Press = 3-4 minutes<br>Auto Drip = 4-5 minutes</p>
    <div class="side-ornament" role="img" aria-label="Small light-blue swirl ornament"></div>
    <svg class="gusset" width="220" height="100" viewBox="0 0 220 100">
      <polyline points="0,100 110,4 220,100" fill="none" stroke="#cee9f5" stroke-width="1.2" stroke-dasharray="5 4"/>
    </svg>
  </section>
</main>
</body>
</html>
```